Project Title:
Dental Implant Overdenture Flyer (Retirement Village Target)
Objective:
Create a clean, trustworthy, and reassuring flyer aimed at older adults (60–85 years old) who struggle with loose dentures. The goal is to educate them about implant-retained “clip-on” dentures and encourage them to book a consultation.
Tone & Feel:
Warm, caring, non-intimidating
Premium but not “salesy”
Medical but easy to understand
Focus on improving quality of life (confidence, eating, comfort)
Target Audience:
Retirees / pensioners
Existing denture wearers
People frustrated with loose or uncomfortable dentures
Key Message:
“You don’t have to live with loose dentures anymore.”
Design Style:
Clean, minimal, modern
Soft colours (blues, greens, warm neutrals)
Easy-to-read large font
High contrast for older eyes
Avoid clutter
Imagery Suggestions:
Smiling older adults (natural, not stocky/overly staged)
Before/after lifestyle (eating, laughing, socialising)
Simple diagram showing denture clipping onto implants
Avoid graphic surgical images
Layout Suggestions:
A5 or DL flyer
Clear sections with headings
Icons for benefits
Strong call-to-action at bottom
HEADLINE (big and bold)
Tired of Loose Dentures?
Discover Secure “Clip-On” Teeth
🔹 PROBLEM SECTION
Do your dentures:
Slip or move when eating?
Make it hard to chew certain foods?
Feel uncomfortable or loose?
Affect your confidence when speaking or smiling?
You’re not alone — and there is a better solution.
🔹 SOLUTION SECTION
Implant-Retained “Clip-On” Dentures
We can secure your denture using just 2 dental implants, allowing your teeth to:
✔ Stay firmly in place
✔ Improve your ability to eat
✔ Feel more comfortable
✔ Boost your confidence
🔹 SIMPLE EXPLANATION (very important)
Small titanium implants are gently placed in the jaw.
Your denture then clips securely onto them, stopping movement.
🔹 PRICE SECTION (highlight this clearly)
$12,000
Includes:
2 dental implants
A brand new custom overdenture
Does not include sedation or extractions (if needed)
🔹 SEDATION
Sedation is available for comfort.
If you hold a pensioner card, you may receive a significant Vantacor rebate, often resulting in minimal out-of-pocket costs for sedation.
🔹 TRUST / REASSURANCE
Experienced implant clinician
Gentle, patient-focused care
Modern technology and techniques
🔹 CALL TO ACTION (VERY IMPORTANT)
Book a Free Consultation
📞 Call: 08 9351 4276
🌐 Visit: www.bravonclinic.com.au
📍 Located near Tallowmere shopping centre
🔹 OPTIONAL TAGLINE
Eat Better. Feel Better. Smile with Confidence Again.
Please include some photos to illustrate what a clip on denture looks like with two implants.

```html
<!DOCTYPE html>
<html lang="en">
<head>
<meta charset="utf-8">
<title>Clip-On Dentures Flyer</title>
<link href="https://fonts.googleapis.com/css2?family=Poppins:wght@500;600;700;800&family=Oswald:wght@500&display=swap" rel="stylesheet">
<style>
  :root {
    --backdrop: #525252;
    --teal-deep: #086f8e;
    --teal: #0a86a6;
    --band: #0096b4;
    --turquoise: #1fd3c9;
    --heading: #13a3bf;
    --aqua-panel: #e2fbfb;
    --ink: #111111;
    --white: #ffffff;
  }
  * { box-sizing: border-box; margin: 0; padding: 0; }
  html, body { width: 879px; height: 1200px; overflow: hidden; }
  body { background: var(--backdrop); font-family: "Poppins", sans-serif; color: var(--ink); position: relative; }

  .flyer { position: absolute; left: 124px; top: 113px; width: 631px; height: 974px; background: var(--white); overflow: hidden; }
  .abs { position: absolute; }

  /* Hero */
  .hero { left: 0; top: 0; width: 631px; height: 263px; }
  .hero-photo { position: absolute; inset: 0; background: linear-gradient(120deg, #c9d8ee 0%, #e6c7d2 45%, #d7e0f1 100%); }
  .hero-shape { position: absolute; inset: 0; }
  .headline { left: 38px; top: 30px; font-weight: 700; font-size: 68px; line-height: 58px; letter-spacing: -2px; color: var(--white); text-transform: uppercase; }
  .headline .accent { color: var(--turquoise); }
  .hero-sub { left: 41px; top: 210px; font-weight: 700; font-size: 21px; color: var(--white); }

  /* Benefits */
  .benefits { left: 20px; top: 263px; width: 590px; height: 305px; background: var(--aqua-panel); border-radius: 0 0 22px 22px; }
  .col-heading { font-weight: 700; font-size: 19px; line-height: 24px; color: var(--heading); }
  .problems { left: 42px; top: 282px; width: 260px; }
  .problem { position: absolute; left: 0; display: flex; align-items: center; gap: 10px; font-weight: 500; font-size: 14.5px; line-height: 18px; }
  .problem-icon { width: 32px; height: 32px; border-radius: 3px; background: var(--band); flex: none; display: flex; align-items: center; justify-content: center; }
  .problem-icon.light { background: var(--turquoise); }
  .reassure { left: 42px; top: 509px; font-weight: 700; font-size: 15.5px; line-height: 21px; color: var(--heading); }
  .divider { left: 315px; top: 282px; width: 1.5px; height: 269px; background: var(--heading); }
  .solution { left: 359px; top: 282px; width: 240px; }
  .solution-body { left: 359px; top: 342px; font-weight: 500; font-size: 14px; line-height: 20px; }
  .benefit { position: absolute; left: 359px; z-index: 2; display: flex; align-items: center; gap: 7px; font-weight: 500; font-size: 14.5px; white-space: nowrap; }
  .photo-small { left: 572px; top: 430px; width: 34px; height: 42px; border-radius: 12px; background: radial-gradient(circle, #f6f0ea 25%, #ef8f9b 75%); z-index: 1; }
  .photo-large { left: 448px; top: 537px; width: 146px; height: 72px; border-radius: 30px; background: radial-gradient(ellipse, #faf6ef 25%, #ec8b98 70%); z-index: 1; }

  .explain-band { left: 25px; top: 571px; width: 580px; height: 52px; background: var(--band); border-radius: 0 0 26px 26px; color: var(--white); font-weight: 700; font-size: 11.3px; line-height: 16px; padding: 10px 0 0 17px; }
  .explain-text { position: relative; z-index: 2; }

  /* Offer cards */
  .card { top: 645px; width: 281px; height: 162px; border-radius: 12px; overflow: hidden; background: var(--aqua-panel); }
  .card-foot { position: absolute; left: 0; bottom: 0; width: 100%; height: 58px; background: var(--band); color: var(--white); font-weight: 600; }
  .price-includes { position: absolute; left: 17px; top: 12px; font-weight: 700; font-size: 11.5px; line-height: 15px; }
  .price { position: absolute; left: 16px; top: 54px; font-weight: 700; font-size: 37px; color: var(--turquoise); letter-spacing: -0.5px; }
  .price-card { left: 25px; }
  .price-card .card-foot { font-size: 12px; line-height: 15.5px; padding: 13px 0 0 17px; }
  .implant-photo { position: absolute; left: 200px; top: 8px; width: 72px; height: 145px; border-radius: 10px; background: linear-gradient(180deg, #f4f4f4 0%, #c9ced3 55%, #a9b0b6 100%); }
  .sedation-card { left: 324px; }
  .sedation-title { position: absolute; left: 17px; top: 14px; font-weight: 700; font-size: 22.5px; line-height: 25px; color: var(--teal); }
  .sedation-title .accent { color: var(--turquoise); }
  .sedation-photo { position: absolute; left: 188px; top: 14px; width: 78px; height: 78px; border-radius: 4px; background: linear-gradient(135deg, #9fd4ef 0%, #4ca6d8 60%, #2b7fbf 100%); }
  .sedation-card .card-foot { font-size: 10.8px; line-height: 14.5px; padding: 7px 0 0 17px; }

  /* Trust row */
  .trust { left: 30px; top: 815px; width: 572px; list-style: none; display: flex; justify-content: space-between; font-family: "Oswald", sans-serif; font-weight: 500; font-size: 12.6px; text-transform: uppercase; letter-spacing: -0.3px; }
  .trust-item { display: flex; align-items: center; gap: 4px; white-space: nowrap; }

  /* Contact */
  .contact { left: 20px; top: 866px; width: 590px; height: 130px; background: var(--aqua-panel); border-radius: 20px 20px 0 0; }
  .brand { left: 45px; top: 898px; display: flex; align-items: center; gap: 8px; font-weight: 600; font-size: 17px; color: var(--teal); }
  .brand-dot { width: 22px; height: 22px; border-radius: 50%; background: var(--turquoise); }
  .phone { left: 218px; top: 886px; display: flex; align-items: center; gap: 3px; font-weight: 700; font-size: 29px; line-height: 36px; }
  .web { left: 220px; top: 917px; font-weight: 600; font-size: 18px; }
  .web .accent { color: var(--heading); }
  .clinician-photo { left: 477px; top: 840px; width: 123px; height: 134px; border-radius: 50px 50px 0 0; background: linear-gradient(180deg, #d9b79a 0%, #c59a7c 45%, #222 70%, #151515 100%); }
</style>
</head>
<body>
<main class="flyer">
  <section class="hero abs">
    <div class="hero-photo" role="img" aria-label="Photo of a pair of full dentures on a pale blue background"></div>
    <svg class="hero-shape" width="631" height="263" viewBox="0 0 631 263" aria-hidden="true">
      <defs>
        <linearGradient id="heroTeal" x1="0" y1="0" x2="1" y2="1">
          <stop offset="0" stop-color="#0a7fa0"/>
          <stop offset="1" stop-color="#086c8b"/>
        </linearGradient>
      </defs>
      <path d="M0 0 H455 Q495 0 493 42 L440 263 H0 Z" fill="url(#heroTeal)" opacity="0.97"/>
    </svg>
    <h1 class="headline abs">Tired<br>of Loose<br><span class="accent">Dentures?</span></h1>
    <p class="hero-sub abs">Discover Secure “Clip-On” Teeth</p>
  </section>

  <div class="benefits abs"></div>

  <section class="problems abs">
    <h2 class="col-heading">Do Your Dentures:</h2>
  </section>
  <div class="problem abs" style="left:43px;top:319px">
    <span class="problem-icon"><svg width="20" height="20" viewBox="0 0 20 20" fill="none" stroke="#fff" stroke-width="1.3"><path d="M3 7 Q10 3 17 7 Q10 11 3 7Z"/><path d="M5 12 Q10 16 15 12"/></svg></span>
    <span>Slip or move<br>when eating?</span>
  </div>
  <div class="problem abs" style="left:43px;top:367px">
    <span class="problem-icon light"><svg width="20" height="20" viewBox="0 0 20 20" fill="none" stroke="#fff" stroke-width="1.3"><path d="M3 7 Q10 3 17 7 Q10 11 3 7Z"/><path d="M5 12 Q10 16 15 12"/></svg></span>
    <span>Make it hard to<br>chew certain foods?</span>
  </div>
  <div class="problem abs" style="left:43px;top:415px">
    <span class="problem-icon"><svg width="20" height="20" viewBox="0 0 20 20" fill="none" stroke="#fff" stroke-width="1.3"><path d="M3 7 Q10 3 17 7 Q10 11 3 7Z"/><path d="M11 11 L14 17"/></svg></span>
    <span>Feel uncomfortable<br>or loose?</span>
  </div>
  <div class="problem abs" style="left:43px;top:463px">
    <span class="problem-icon light"><svg width="20" height="20" viewBox="0 0 20 20" fill="none" stroke="#fff" stroke-width="1.3"><path d="M10 3 V9 Q8 11 7 10"/><path d="M5 14 Q10 17 15 14"/></svg></span>
    <span>Affect your confidence<br>when speaking or smiling?</span>
  </div>
  <p class="reassure abs">You’re not Alone<br>and There is a Better Solution.</p>

  <div class="divider abs"></div>

  <section class="solution abs">
    <h2 class="col-heading">Implant-Retained<br>“Clip-On” Dentures</h2>
  </section>
  <p class="solution-body abs">We Can Secure Your Denture<br>Using Just 2 Dental Implants,<br>Allowing Your Teeth To:</p>
  <div class="benefit" style="top:412px"><svg width="15" height="15" viewBox="0 0 16 16" fill="none" stroke="#13a3bf" stroke-width="1.6"><circle cx="8" cy="8" r="6.8"/><path d="M4.8 8.2 L7.2 10.5 L11.5 5.6"/></svg>Stay firmly in place</div>
  <div class="benefit" style="top:442px"><svg width="15" height="15" viewBox="0 0 16 16" fill="none" stroke="#13a3bf" stroke-width="1.6"><circle cx="8" cy="8" r="6.8"/><path d="M4.8 8.2 L7.2 10.5 L11.5 5.6"/></svg>Improve your ability to eat</div>
  <div class="benefit" style="top:471px"><svg width="15" height="15" viewBox="0 0 16 16" fill="none" stroke="#13a3bf" stroke-width="1.6"><circle cx="8" cy="8" r="6.8"/><path d="M4.8 8.2 L7.2 10.5 L11.5 5.6"/></svg>Feel more comfortable</div>
  <div class="benefit" style="top:501px"><svg width="15" height="15" viewBox="0 0 16 16" fill="none" stroke="#13a3bf" stroke-width="1.6"><circle cx="8" cy="8" r="6.8"/><path d="M4.8 8.2 L7.2 10.5 L11.5 5.6"/></svg>Boost your confidence</div>
  <div class="photo-small abs" role="img" aria-label="Photo of a full denture set"></div>

  <div class="explain-band abs"><p class="explain-text">Small Titanium Implants are Gently Placed in The Jaw.<br>Your Denture Then Clips Securely Onto Them, Stopping Movement.</p></div>
  <div class="photo-large abs" role="img" aria-label="Photo of a denture clipping onto two implants"></div>

  <section class="card price-card abs">
    <p class="price-includes">2 Dental Implants<br>A Brand New Custom<br>Overdenture</p>
    <p class="price">$12,000</p>
    <div class="card-foot">Does Not Include Sedation<br>Or Extractions (If Needed)</div>
    <div class="implant-photo" role="img" aria-label="Photo of titanium dental implants with crowns"></div>
  </section>

  <section class="card sedation-card abs">
    <h2 class="sedation-title"><span class="accent">Sedation</span> is<br>Available for<br>Comfort.</h2>
    <div class="sedation-photo" role="img" aria-label="Photo of a relaxed patient receiving sedation"></div>
    <p class="card-foot">If you hold a pensioner card, you may receive<br>a significant Vantacor rebate, often resulting<br>in minimal out-of-pocket costs for sedation.</p>
  </section>

  <ul class="trust abs">
    <li class="trust-item"><svg width="15" height="15" viewBox="0 0 16 16" fill="none" stroke="#13a3bf" stroke-width="1.6"><circle cx="8" cy="8" r="6.8"/><path d="M4.8 8.2 L7.2 10.5 L11.5 5.6"/></svg>Experienced Implant Clinician</li>
    <li class="trust-item"><svg width="15" height="15" viewBox="0 0 16 16" fill="none" stroke="#13a3bf" stroke-width="1.6"><circle cx="8" cy="8" r="6.8"/><path d="M4.8 8.2 L7.2 10.5 L11.5 5.6"/></svg>Gentle, Patient-Focused Care</li>
    <li class="trust-item"><svg width="15" height="15" viewBox="0 0 16 16" fill="none" stroke="#13a3bf" stroke-width="1.6"><circle cx="8" cy="8" r="6.8"/><path d="M4.8 8.2 L7.2 10.5 L11.5 5.6"/></svg>Modern Technology and Techniques</li>
  </ul>

  <div class="contact abs"></div>
  <div class="brand abs"><span class="brand-dot"></span>Bravon Clinic</div>
  <p class="phone abs"><svg width="26" height="26" viewBox="0 0 26 26"><circle cx="13" cy="13" r="12" fill="#13a3bf"/><path d="M9 7 L11 7 L12 10.5 L10.6 11.8 Q12 14.6 14.2 15.6 L15.5 14.2 L19 15.2 L19 17.2 Q18 19 15.6 18.6 Q9.5 16.8 7.6 10.4 Q7.4 8 9 7Z" fill="#fff"/></svg>08 9351 4276</p>
  <p class="web abs">www.<span class="accent">bravonclinic</span>.com.au</p>
  <div class="clinician-photo abs" role="img" aria-label="Photo of the smiling implant clinician in dark scrubs"></div>
</main>
</body>
</html>
```